Local Directory Ad

We currently have an advertisement in our local directory (see attached). We would like to make it look more appealing.
Dimensions are 110mm H X 175mm W
We would like to keep the same colours and contact details remain the same.
Most of the content can remain the same, Just remove the line Tax effective remote area salary packaging and add in Self Managed Super Funds.We want to change mortgage broking to Mortgage Broking and Loan Structuring.

We want to change the line Local accountants Local Knowledge Local Experience - to something like local knowledge beyond compare or unsurpassed local knowledge but open to suggestions on this.

there are some good designs posted so far. I particulalry like the ones from marloquip, tovel58, and the last one posted by pruvsomlak and WPH. Keep up the good work guys

```html
<!DOCTYPE html>
<html lang="en">
<head>
<meta charset="utf-8">
<title>Brindle Accounting &amp; Finance – Directory Ad</title>
<link rel="stylesheet" href="https://fonts.googleapis.com/css2?family=Crimson+Text:wght@400;600;700&family=Open+Sans:wght@400;600;700&display=swap">
<style>
  :root {
    --navy: #454672;
    --navy-light: #6c76a6;
    --red: #d93237;
    --red-deep: #9c1b17;
    --red-bright: #d8261b;
    --yellow: #ece11b;
    --white: #ffffff;
    --frame: #c9c9c9;
    --ink: #111111;
  }
  * { margin: 0; padding: 0; box-sizing: border-box; }
  html, body { width: 1200px; height: 808px; overflow: hidden; background: var(--white); }
  .canvas { position: relative; width: 1200px; height: 808px; background: var(--white); }
  .ad-frame { position: absolute; left: 78px; top: 76px; width: 1029px; height: 649px; border: 1px solid var(--frame); }
  .side-bar { position: absolute; background: var(--navy); }
  .side-bar--left { left: 85px; top: 80px; width: 53px; height: 644px; border-top-left-radius: 22px; }
  .side-bar--left-accent { left: 110px; top: 80px; width: 28px; height: 334px; background: var(--navy-light); border-bottom-left-radius: 16px; }
  .side-bar--right { left: 1052px; top: 80px; width: 54px; height: 644px; border-top-right-radius: 22px; }
  .top-band { position: absolute; left: 151px; top: 82px; width: 889px; height: 51px; background: var(--navy); }
  .category-tab { position: absolute; left: 151px; top: 82px; width: 303px; height: 51px; background: var(--yellow); border-top-right-radius: 16px;
    font-family: "Open Sans", sans-serif; font-weight: 600; font-size: 31px; color: var(--ink); padding-left: 24px; line-height: 50px; }
  .name-panel { position: absolute; left: 151px; top: 141px; width: 889px; height: 151px; background: var(--red);
    border-top-right-radius: 34px; border-bottom-left-radius: 22px; color: var(--white); overflow: hidden; }
  .business-name { position: absolute; left: 50%; top: 14px; white-space: nowrap;
    font-family: "Crimson Text", serif; font-weight: 400; font-size: 80px; line-height: 1;
    transform: translateX(-50%) scaleX(0.88); }
  .licence { position: absolute; left: 0; right: 0; top: 112px; text-align: center; white-space: nowrap;
    font-family: "Open Sans", sans-serif; font-size: 24px; line-height: 32px; }
  .tagline { position: absolute; left: 151px; top: 296px; width: 889px; text-align: center; white-space: nowrap;
    font-family: "Crimson Text", serif; font-weight: 700; font-size: 58px; color: var(--red); text-shadow: 2px 2px 0 var(--navy); }
  .services-panel { position: absolute; left: 151px; top: 378px; width: 889px; height: 167px; background: var(--navy);
    border-top-right-radius: 30px; color: var(--white); text-align: center; }
  .services-heading { font-family: "Crimson Text", serif; font-weight: 700; font-size: 40px; margin-top: 6px; line-height: 1.1; white-space: nowrap; }
  .service-row { font-family: "Open Sans", sans-serif; font-size: 25px; line-height: 35px; white-space: nowrap; }
  .service-item::before { content: ""; display: inline-block; width: 11px; height: 11px; border-radius: 50%; background: var(--yellow); margin: 0 7px 3px 0; vertical-align: middle; }
  .service-item + .service-item { margin-left: 14px; }
  .contact-panel { position: absolute; left: 151px; top: 551px; width: 889px; height: 108px; background: var(--navy);
    border-bottom-left-radius: 22px; color: var(--white); font-family: "Open Sans", sans-serif; font-size: 21px; line-height: 31px; }
  .contact-address { position: absolute; left: 46px; top: 7px; font-style: normal; }
  .contact-direct { position: absolute; right: 42px; top: 7px; text-align: right; }
  .web-band { position: absolute; left: 151px; top: 666px; width: 889px; height: 52px;
    background: linear-gradient(90deg, var(--red-deep) 0%, var(--red-bright) 50%, var(--red-deep) 100%);
    border-top-right-radius: 22px; text-align: center; color: var(--white);
    font-family: "Open Sans", sans-serif; font-weight: 700; font-size: 23px; line-height: 52px; }
</style>
</head>
<body>
<div class="canvas">
  <div class="ad-frame"></div>
  <div class="side-bar side-bar--left"></div>
  <div class="side-bar side-bar--left-accent"></div>
  <div class="side-bar side-bar--right"></div>
  <div class="top-band"></div>
  <div class="category-tab">Accountants</div>

  <div class="name-panel">
    <h1 class="business-name">Brindle Accounting &amp; Finance</h1>
    <p class="licence">Australian Credit Licence 512 846</p>
  </div>

  <p class="tagline">Local knowledge beyond compare</p>

  <div class="services-panel">
    <h2 class="services-heading">We are here for you all year round to assist with...</h2>
    <p class="service-row"><span class="service-item">Accouning &amp; Taxation</span><span class="service-item">Business Advice</span><span class="service-item">GST and BAS’s</span></p>
    <p class="service-row"><span class="service-item">Mortgage Broking and Loan Structuring</span><span class="service-item">Bookkeeping</span></p>
    <p class="service-row"><span class="service-item">Self Managed Super Funds for your employees</span></p>
  </div>

  <div class="contact-panel">
    <address class="contact-address">
      Shop 3 Harbour Walk<br>
      12 Lindell St Port Avalon<br>
      PO Box 418 Port Avalon 6790
    </address>
    <div class="contact-direct">
      reception @baaf.com.an<br>
      Ph: 9250 4183<br>
      Fax: 9381 6027
    </div>
  </div>

  <div class="web-band">www.baaf.com.au</div>
</div>
</body>
</html>
```